Free Printer Promotion

Hi i need a banner AD for my website.

The promotion is: free printer, for a monthly cost you get all the supplies and service included. Its a subscription service for printing. There is 5 plans available.
Prices vary upon printers, most expensive plan is $69.94 a month for a 1 year term and the most affordable plan is $9.95 a month for 3 year term

1 Monochrome laser (print only printer, black and white printing)
2 Multifunction Monochrome laser (print scan copy fax printer, black and white printing)

• Monochrome Printers are given 1000 prints per month
• Toner included
• Service included
• Printer included

3 Color laser (print only printer, color printing)
4 Multifunction Color laser (print scan copy fax, color printing)
Color printers are given 500 monochrome prints and 500 color prints per month
• Toner included
• Service included
• Printer included

5 Inkjet color printer (print copy scan fax, color printing)
• Inkjet Printers are given 1000 prints per month.
• Ink included
• Service included
• Printer included

Target Market(s)

students, home office workers, corporate business and government

Font styles to use
Serif
Sans Serif

Requirements
Must have
• i want it to be enticing, no long sentences. the customer will click on the banner and it will bring them to another page with the information.

Keep it short and sweet.

```html
<!DOCTYPE html>
<html lang="en">
<head>
<meta charset="UTF-8">
<title>Printer Promotion Banner</title>
<link rel="stylesheet" href="https://fonts.googleapis.com/css2?family=Oswald:wght@600;700&family=Special+Elite&family=Montserrat:wght@800&display=swap">
<style>
  :root {
    --teal-deep: #0c3d48;
    --teal-mid: #0f7a86;
    --teal-bright: #22c3c8;
    --paper: #ffffff;
    --tag-yellow: #fde418;
    --ink: #0b0b0b;
    --label-text: #ffffff;
    --printer-light: #eef1f2;
    --printer-shade: #c9d0d3;
  }
  * { margin: 0; padding: 0; box-sizing: border-box; }
  html, body { width: 1200px; height: 675px; overflow: hidden; background: var(--paper); }
  .banner {
    position: relative;
    width: 1200px;
    height: 675px;
    overflow: hidden;
    background:
      radial-gradient(ellipse 60% 70% at 72% 48%, var(--teal-bright) 0%, rgba(34,195,200,0) 70%),
      linear-gradient(100deg, var(--teal-deep) 0%, var(--teal-mid) 45%, #159aa2 100%);
  }
  .torn-edges { position: absolute; inset: 0; width: 1200px; height: 675px; }
  .headline-tag {
    position: absolute;
    left: 88px;
    top: 70px;
    width: 560px;
    height: 72px;
    transform: rotate(-2deg);
  }
  .headline-tag__frame {
    position: absolute;
    left: -6px; top: -12px;
    width: 572px; height: 94px;
    border: 3px solid var(--paper);
    transform: rotate(1.5deg);
  }
  .headline-tag__fill {
    position: absolute;
    inset: 0;
    background: var(--tag-yellow);
    display: flex;
    align-items: center;
    justify-content: center;
  }
  .headline-tag__text {
    font-family: "Oswald", sans-serif;
    font-weight: 700;
    font-size: 38px;
    letter-spacing: 5px;
    color: var(--ink);
    text-transform: uppercase;
  }
  .plan-list { position: absolute; left: 116px; top: 208px; list-style: none; }
  .plan-list__item {
    display: block;
    width: max-content;
    background: var(--ink);
    color: var(--label-text);
    font-family: "Special Elite", monospace;
    font-size: 30px;
    line-height: 1;
    padding: 9px 16px 8px 14px;
    margin-bottom: 13px;
  }
  .plan-list__item:nth-child(2) { transform: translateX(4px); }
  .plan-list__item:nth-child(4) { padding-top: 11px; padding-bottom: 10px; }
  .plan-list__item:nth-child(5) { transform: translateX(6px); padding-top: 11px; padding-bottom: 10px; }
  .product-visual {
    position: absolute;
    left: 790px;
    top: 110px;
    width: 300px;
    height: 320px;
    border-radius: 14px;
    background: linear-gradient(160deg, var(--printer-light) 0%, var(--printer-shade) 100%);
    opacity: 0.92;
  }
  .shop-button {
    position: absolute;
    left: 874px;
    top: 494px;
    width: 202px;
    height: 62px;
    border-radius: 31px;
    background: var(--tag-yellow);
    color: var(--ink);
    font-family: "Montserrat", sans-serif;
    font-weight: 800;
    font-size: 24px;
    display: flex;
    align-items: center;
    justify-content: center;
    text-decoration: none;
  }
</style>
</head>
<body>
<main class="banner">
  <svg class="torn-edges" viewBox="0 0 1200 675" aria-hidden="true">
    <polygon fill="#ffffff" points="950,0 1200,0 1200,62 1182,58 1170,66 1150,52 1132,60 1118,46 1100,50 1086,38 1068,42 1050,30 1032,34 1016,22 998,24 982,12 966,14"/>
    <polygon fill="#ffffff" points="0,600 30,606 62,596 96,604 130,598 170,610 210,602 250,614 300,606 340,618 380,610 430,620 470,612 520,622 560,616 610,626 650,618 700,628 740,620 790,630 830,622 880,632 920,624 960,634 1000,626 1050,636 1090,628 1140,638 1170,630 1200,634 1200,675 0,675"/>
  </svg>

  <div class="headline-tag">
    <div class="headline-tag__frame"></div>
    <div class="headline-tag__fill"><span class="headline-tag__text">Printer Promotion</span></div>
  </div>

  <ul class="plan-list">
    <li class="plan-list__item">Monochrome laser</li>
    <li class="plan-list__item">Multifunction Monochrome laser</li>
    <li class="plan-list__item">Color laser</li>
    <li class="plan-list__item">Multifunction Color laser</li>
    <li class="plan-list__item">Inkjet color printer</li>
  </ul>

  <div class="product-visual" role="img" aria-label="White home inkjet printer with paper loaded"></div>

  <a class="shop-button" href="#">SHOP NOW</a>
</main>
</body>
</html>
```